Website for Apartment Rental in Prague

I would like to create designs of my website focused on luxury apartment rentals in Prague, Czech Republic. I created initial mock-ups, They are all attached. I need to design homepage and subpage. The mock-ups were created by combining elements from different websites that I liked but I need you to create a design that is unique and original. The attached files a only a guidance for the structure of the website but not for the design. Try to be creative.

Industry/Entity Type

Apartment

```html
<!DOCTYPE html>
<html lang="en">
<head>
<meta charset="utf-8">
<title>Lumen Residences – Being Home in Prague</title>
<link rel="stylesheet" href="https://fonts.googleapis.com/css2?family=Nunito:wght@400;600;700&display=swap">
<style>
:root{
  --teal:#125a74;
  --teal-bright:#1a6a88;
  --ink:#1f1f22;
  --body:#222225;
  --field:#e6e7e9;
  --field-text:#6d6f73;
  --white:#ffffff;
  --dot:#3c3c40;
  --hero-a:#9fc1dc;
  --hero-b:#5a88c2;
  --hero-c:#d9e3ee;
}
*{box-sizing:border-box;margin:0;padding:0}
html,body{width:880px;height:1200px;overflow:hidden;background:var(--white)}
body{font-family:"Nunito",sans-serif;color:var(--ink)}
.page{position:relative;width:880px;height:1200px}

/* header */
.brand{position:absolute;left:75px;top:46px;display:flex;align-items:center;gap:14px}
.brand-square{width:52px;height:52px;background:var(--teal)}
.brand-name{font-size:22px;font-weight:700;color:var(--teal);line-height:26px}

.contact-icons{position:absolute;top:60px;left:724px;display:flex;gap:11px}
.contact-icons a{width:35px;height:35px;border-radius:50%;background:var(--teal);display:flex;align-items:center;justify-content:center}

.main-nav a{position:absolute;top:140px;font-size:18px;color:var(--ink);text-decoration:none;letter-spacing:.3px;white-space:nowrap}
.main-nav a.active{color:var(--teal-bright)}

/* hero */
.hero{position:absolute;left:0;top:171px;width:880px;height:471px;overflow:hidden}
.hero-photo{position:absolute;inset:0;background:linear-gradient(100deg,var(--hero-a) 0%,#6d98c4 30%,var(--hero-b) 55%,#8fb0d6 78%,var(--hero-c) 100%)}
.hero-title{position:absolute;left:510px;top:164px;color:var(--ink);font-weight:600;line-height:1}
.hero-title .line1{display:block;font-size:41px;letter-spacing:-1px}
.hero-title .line2{display:flex;align-items:baseline;gap:10px;margin-top:8px}
.hero-title .small{font-size:40px;letter-spacing:-1px}
.hero-title .big{font-size:60px;font-weight:700;letter-spacing:-1px}

.booking-bar{position:absolute;left:0;top:375px;width:880px;height:96px;background:rgba(120,170,205,.55)}
.field{position:absolute;top:31px;width:150px;height:32px;background:var(--field);color:var(--field-text);font-size:13.5px;padding:7px 11px}
.book-btn{position:absolute;left:604px;top:31px;width:218px;height:32px;background:var(--teal);color:var(--white);font-size:16px;font-weight:600;display:flex;align-items:center;justify-content:center}

/* rooms */
.rooms-title{position:absolute;left:150px;top:742px;font-size:30px;font-weight:600;color:var(--teal)}
.rooms-rule{position:absolute;left:150px;top:782px;width:54px;height:6px;background:var(--teal)}
.rooms-text{position:absolute;left:75px;top:810px;width:400px;font-size:14px;line-height:16px;color:var(--body);white-space:nowrap}
.rooms-photo{position:absolute;left:522px;top:711px;width:358px;height:209px;background:linear-gradient(160deg,#e2e4e6 0%,#c8ccd2 35%,#2c56a8 60%,#3a3c45 85%,#9a7a5a 100%)}
.slider-dots{position:absolute;top:938px;left:672px;display:flex;gap:9px;align-items:center}
.slider-dots span{width:13px;height:13px;border-radius:50%;background:var(--dot)}
.slider-dots span.active{width:16px;height:16px;background:var(--teal)}

/* footer */
.site-footer{position:absolute;left:0;top:1009px;width:880px;height:191px;background:var(--teal);color:var(--white)}
.footer-map{position:absolute;left:75px;top:81px}
.footer-address{position:absolute;left:134px;top:76px;font-size:13.5px;line-height:16px}
.footer-contact{position:absolute;left:321px;top:79px;font-size:10px;font-weight:600}
.footer-contact div{display:flex;align-items:center;gap:14px;height:26px}
.footer-contact svg{width:22px}
.footer-legal{position:absolute;left:673px;top:84px;font-size:10px;font-weight:600}
.footer-legal .links{display:flex;gap:27px}
.footer-legal .copy{display:flex;align-items:center;gap:6px;margin-top:8px}
.copy-mark{width:12px;height:12px;border-radius:50%;background:var(--white);color:var(--teal);font-size:9px;font-weight:700;display:flex;align-items:center;justify-content:center}
</style>
</head>
<body>
<div class="page">
  <header>
    <div class="brand">
      <div class="brand-square"></div>
      <div class="brand-name">Lumen<br>Residences</div>
    </div>
    <div class="contact-icons">
      <a aria-label="Email"><svg width="20" height="14" viewBox="0 0 20 14"><rect x="1" y="1" width="18" height="12" fill="none" stroke="#fff" stroke-width="1.6"/><path d="M1 1l9 7 9-7M1 13l7-6M19 13l-7-6" fill="none" stroke="#fff" stroke-width="1.4"/></svg></a>
      <a aria-label="Phone"><svg width="18" height="18" viewBox="0 0 24 24"><path fill="#fff" d="M6.6 10.8a15.1 15.1 0 006.6 6.6l2.2-2.2c.3-.3.7-.4 1-.2 1.1.4 2.3.6 3.6.6.6 0 1 .4 1 1V20c0 .6-.4 1-1 1A17 17 0 013 4c0-.6.4-1 1-1h3.5c.6 0 1 .4 1 1 0 1.3.2 2.5.6 3.6.1.3 0 .7-.2 1l-2.3 2.2z"/></svg></a>
    </div>
    <nav class="main-nav">
      <a class="active" style="left:219px">APARTMENT</a>
      <a style="left:366px">NEWS</a>
      <a style="left:462px">GALLERIES</a>
      <a style="left:600px">ABOUT</a>
    </nav>
  </header>

  <section class="hero">
    <div class="hero-photo" role="img" aria-label="Bright blue and white apartment bedroom with a balcony overlooking the sea"></div>
    <h1 class="hero-title"><span class="line1">BEING HOME</span><span class="line2"><span class="small">IN</span><span class="big">PRAGUE</span></span></h1>
    <div class="booking-bar">
      <div class="field" style="left:74px">Check in Date</div>
      <div class="field" style="left:242px">Check out Date</div>
      <div class="field" style="left:410px">Room Type</div>
      <div class="book-btn">Book Your Room</div>
    </div>
  </section>

  <section class="rooms">
    <h2 class="rooms-title">The Rooms</h2>
    <div class="rooms-rule"></div>
    <p class="rooms-text">Lorem Ipsum is simply dummy text of the printing and<br>typesetting industry. Lorem Ipsum has been the industry's<br>standard dummy text ever since the 1500s, when an<br>unknown printer took a galley of type and scrambled it<br>to make a type specimen book.</p>
    <div class="rooms-photo" role="img" aria-label="Apartment bedroom with white bed, blue headboard and striped rug"></div>
    <div class="slider-dots"><span class="active"></span><span></span><span></span></div>
  </section>

  <footer class="site-footer">
    <svg class="footer-map" width="40" height="36" viewBox="0 0 40 36" aria-hidden="true"><path fill="#fff" d="M0 4l12-4v32L0 36zM14 0l12 4v32l-12-4zM28 4l12-4v32l-12 4z"/></svg>
    <div class="footer-address">Kamenná 27<br>120 00 Prague<br>CZECH REPUBLIC</div>
    <div class="footer-contact">
      <div><svg viewBox="0 0 22 16" height="16"><rect x="1" y="1" width="20" height="14" fill="none" stroke="#fff" stroke-width="1.6"/><path d="M1 1l10 8 10-8M1 15l8-7M21 15l-8-7" fill="none" stroke="#fff" stroke-width="1.4"/></svg>booking@lumenresidences.com</div>
      <div><svg viewBox="0 0 24 24" height="20"><path fill="#fff" d="M6.6 10.8a15.1 15.1 0 006.6 6.6l2.2-2.2c.3-.3.7-.4 1-.2 1.1.4 2.3.6 3.6.6.6 0 1 .4 1 1V20c0 .6-.4 1-1 1A17 17 0 013 4c0-.6.4-1 1-1h3.5c.6 0 1 .4 1 1 0 1.3.2 2.5.6 3.6.1.3 0 .7-.2 1l-2.3 2.2z"/></svg>+420 600 123 456</div>
    </div>
    <div class="footer-legal">
      <div class="links"><span>Privacy Policy</span><span>Sitemap</span></div>
      <div class="copy"><span class="copy-mark">c</span>2017&nbsp; lumenresidences.com</div>
    </div>
  </footer>
</div>
</body>
</html>
```